US Recruiting Firm Needs Dynamic Tri-Fold Brochure

Need tri-fold professional brochure for HR recruiting and consulting firm based in the US.

Target Market(s)

Clients seeking administrative and human resources talent

Industry/Entity Type

Recruitment

Font styles to use
Sans Serif

Requirements
Should not have
• No weird shapes
• No heavy geometric shapes -- I prefer curvy lines
• Not a dark brochure

```html
<!DOCTYPE html>
<html lang="en">
<head>
<meta charset="utf-8">
<title>Piedmont Talent Partners – Tri-Fold Brochure</title>
<link href="https://fonts.googleapis.com/css2?family=Lato:wght@400;700&family=Libre+Baskerville:wght@400&display=swap" rel="stylesheet">
<style>
  :root {
    --stage: #d7d9dc;
    --paper: #ffffff;
    --ink: #2b2b2b;
    --navy: #0f2c4c;
    --navy-deep: #0a1f38;
    --royal: #1d4f9a;
    --orange: #f26a0f;
    --green: #8cc63f;
    --tag: #111111;
    --muted: #f1f3f5;
  }
  * { box-sizing: border-box; margin: 0; padding: 0; }
  html, body { width: 1200px; height: 903px; overflow: hidden; }
  body {
    background: var(--stage);
    font-family: "Lato", sans-serif;
    color: var(--ink);
  }
  .spread {
    position: absolute; left: 20px; top: 11px;
    width: 1160px; height: 880px;
    display: grid; grid-template-columns: repeat(3, 1fr);
    background: var(--paper);
    box-shadow: 0 4px 18px rgba(0,0,0,.18);
  }
  .panel { position: relative; overflow: hidden; }

  /* About panel */
  .about { background: linear-gradient(90deg, #fff 80%, #f3f4f6 100%); }
  .about-copy { position: absolute; left: 42px; right: 41px; top: 42px; }
  .section-tag {
    display: inline-block; background: var(--tag); color: #fff;
    font: 700 13.5px "Lato", sans-serif; padding: 2px 20px 2px 6px;
    clip-path: polygon(0 0, 100% 0, 86% 100%, 0 100%);
    margin-bottom: 14px;
  }
  .about-copy p {
    font-size: 12px; line-height: 15.6px; text-align: justify;
    color: #3a3a3a; margin-bottom: 15px;
  }
  .about-photo {
    position: absolute; left: 0; right: 0; top: 455px; bottom: 0;
    background: linear-gradient(160deg, #f4f5f7 0%, #cfd6dd 35%, #2f8fb3 70%, #e6c79d 100%);
  }
  .web-band {
    position: absolute; left: 0; right: 0; top: 815px; height: 26px;
    background: var(--navy); color: #fff; font-size: 13px;
    display: flex; align-items: center; justify-content: center;
  }

  /* Contact panel */
  .contact { background: linear-gradient(180deg, #fff 40%, #eef0f2 100%); }
  .team-photo {
    position: absolute; left: 0; right: 0; top: 0; height: 335px;
    background: linear-gradient(180deg, #e9edf1 0%, #aeb8c3 35%, #6d7985 60%, #ffffff 100%);
  }
  .brand-mark {
    position: absolute; left: 0; right: 0; top: 400px;
    display: flex; align-items: center; justify-content: center; gap: 10px;
  }
  .brand-dot { width: 22px; height: 22px; border-radius: 50%; background: var(--navy); }
  .brand-name {
    font: 400 21px "Libre Baskerville", serif; color: var(--navy);
    text-transform: uppercase; line-height: 1.2; text-align: center;
  }
  .contact-block { position: absolute; left: 0; right: 0; top: 611px; text-align: center; }
  .contact-title {
    display: inline-block; background: var(--navy); color: #fff;
    font: 400 16px "Lato", sans-serif; letter-spacing: .3px; padding: 3px 9px;
  }
  .contact-lead { font-size: 13.5px; line-height: 17px; margin: 14px auto 14px; width: 170px; }
  .contact-item { font-size: 13.5px; margin-bottom: 13px; }
  .contact-item svg { display: block; margin: 0 auto 2px; }

  /* Cover panel */
  .cover { background: var(--navy-deep); }
  .cover-head {
    position: absolute; left: 0; right: 0; top: 0; height: 155px;
    background: #fff; border-bottom: 5px solid var(--orange);
    display: flex; flex-direction: column; align-items: center; justify-content: center;
  }
  .cover-brand { display: flex; align-items: center; gap: 10px; }
  .cover-brand .brand-name { font-size: 22px; }
  .tagline { font: 700 12.5px "Lato", sans-serif; color: #111; margin-top: 4px; margin-left: 30px; }
  .cover-photo {
    position: absolute; left: 0; right: 0; top: 155px; height: 485px;
    background: linear-gradient(180deg, #0d3a86 0%, #2a6bc4 35%, #5c6b7d 70%, #dfe3e7 100%);
    border-bottom: 3px solid var(--green);
  }
  .cover-title {
    position: absolute; left: 0; right: 0; top: 695px; text-align: center;
    font-family: "Libre Baskerville", serif; text-transform: uppercase;
  }
  .cover-title .lead { color: #fff; font-size: 31px; letter-spacing: .5px; }
  .cover-title .line-orange { color: var(--orange); font: 400 17px "Lato", sans-serif; letter-spacing: .3px; margin-top: 2px; }
  .cover-title .line-green { color: var(--green); font-size: 17px; margin-top: 4px; }
  .cover-band {
    position: absolute; left: 0; right: 0; top: 834px; height: 24px;
    background: var(--orange); color: var(--navy);
    font-size: 13px; display: flex; align-items: center; justify-content: center;
  }
</style>
</head>
<body>
<main class="spread">

  <section class="panel about">
    <div class="about-copy">
      <span class="section-tag">About Us</span>
      <p>Piedmont Talent Partners is a recruiting and search firm that specializes in providing top-notch administrative, professional, and executive level human resources talent.</p>
      <p>We provide best-in-class talent to companies seeking to simplify their recruiting process, increase efficiency, and optimize productivity. Each search is customized based on our client's requirements. We provide quality, timely, and efficient services. Our recruiters are highly skilled in identifying, screening, interviewing, and assessing candidates across various industries. We develop a partnership with our client and candidate in order to make the recruitment process a success for both parties.</p>
      <p>At Piedmont Talent Partners, competence + talent emerge. We are experienced human resources professionals exclusively dedicated to recruiting and placing human resources professionals. We do we love and know for sure: human resources recruiting and consulting. We help awesome companies attract and retain the best employees, increase their profits, and optimize productivity.</p>
    </div>
    <div class="about-photo" role="img" aria-label="Photo of a smiling recruiter talking on a desk phone in a bright office"></div>
    <div class="web-band">Website – to be determined</div>
  </section>

  <section class="panel contact">
    <div class="team-photo" role="img" aria-label="Photo of business people in silhouette meeting in a glass office tower"></div>
    <div class="brand-mark">
      <span class="brand-dot"></span>
      <span class="brand-name">Piedmont<br>Talent Partners</span>
    </div>
    <div class="contact-block">
      <span class="contact-title">CONTACT US</span>
      <p class="contact-lead">To learn more and request a FREE consultation, contact us today.</p>
      <div class="contact-item">
        <svg width="14" height="14" viewBox="0 0 24 24"><path fill="#1d4f9a" d="M6.6 10.8a15 15 0 0 0 6.6 6.6l2.2-2.2a1 1 0 0 1 1-.25 11.4 11.4 0 0 0 3.6.57 1 1 0 0 1 1 1V20a1 1 0 0 1-1 1A17 17 0 0 1 3 4a1 1 0 0 1 1-1h3.5a1 1 0 0 1 1 1c0 1.25.2 2.45.57 3.57a1 1 0 0 1-.25 1z"/></svg>
        Phone to be determined
      </div>
      <div class="contact-item">
        <svg width="15" height="12" viewBox="0 0 24 18"><rect x="1" y="1" width="22" height="16" fill="#1d4f9a"/><path d="M1 1l11 9 11-9" fill="none" stroke="#fff" stroke-width="2"/></svg>
        Email to be determined
      </div>
      <div class="contact-item">
        <svg width="14" height="14" viewBox="0 0 24 24" fill="none" stroke="#1d4f9a" stroke-width="2"><circle cx="12" cy="12" r="10"/><path d="M2 12h20M12 2c3 3 3 17 0 20M12 2c-3 3-3 17 0 20"/></svg>
        Website – to be determined
      </div>
    </div>
  </section>

  <section class="panel cover">
    <header class="cover-head">
      <div class="cover-brand">
        <span class="brand-dot"></span>
        <span class="brand-name">Piedmont<br>Talent Partners</span>
      </div>
      <p class="tagline">Human Resources Staffing &amp; Consulting</p>
    </header>
    <div class="cover-photo" role="img" aria-label="Photo of smiling business team shaking hands over a meeting table in front of a glowing blue world map"></div>
    <div class="cover-title">
      <div class="lead">Specializing in</div>
      <div class="line-orange">ADMINISTRATIVE, PROFESSIONAL,</div>
      <div class="line-green">and Executive HR Talent</div>
    </div>
    <div class="cover-band">Website – to be determined</div>
  </section>

</main>
</body>
</html>
```